Fast Money - Simple Book Cover Design

Hello,

I am in need of a cover for my new book. The Book Title Is

"Standing Growth - Keys to Glowing Customer Ratings That Fill The Calendar and Draw Fresh Clients Through Every Entrance!"

Author: Fireman Dale Orsworth

What I want: This is a book for businesses on improving their online reputation. I want to have 5 Stars on the cover. You can look at this quarvex search for ideas of what I am meaning.....

(copy and paste)

http://www.quarvex-find.example/search?q=5+star+online+reviews&mode=images&ref=kx7Lp2QwZt9 (copy and paste)

I am open to different color schemes for the book. I am partial to dark blues if you make it look good. Here is another book that I really like the cover of....

http://www.brindlemart.example/Clipwave-Tactics-Earning-Promotion-ebook/item/Z93KT4WQPX

I want the cover BOLD and to STAND OUT.

I am looking for a design to help establish me as an authority for online reputation marketing. This book will be both in Pagely format and be used in print as well.

I am open to questions....

Thanks!

Dale

Reason: I don't believe we have received the right designs. I am going to give everyone more time...

Reason: Hi everyone, I had some stuff come up and was not able to be involved in this project. I am extending because we have not seen the exact thing we want and need time to work with designers to get it right. Thanks Dale

Reason: I am currently traveling and can't wrap this up until I get back.

Target Market(s)

Business Owners

Industry/Entity Type

Business

Requirements
Must have
• Title and Subtitle

Author Name

5 Stars Images....
Nice to have
• Creativity

Bold and stand out

Professional

Should not have
• thin text, small to read text, lame graphics,

```html
<!DOCTYPE html>
<html lang="en">
<head>
<meta charset="utf-8">
<title>Standing Growth – Book Cover Spread</title>
<link rel="stylesheet" href="https://fonts.googleapis.com/css2?family=Sansita:wght@700;800;900&display=swap">
<style>
  :root {
    --paper: #ffffff;
    --gold-pale: #fbf1c8;
    --gold: #f0c537;
    --gold-deep: #e0ad1e;
    --gold-amber: #d69f2e;
    --bronze: #8a5a12;
    --bronze-dark: #6b420c;
    --title-gold: #b07a14;
    --star-light: #f7d66a;
    --star-dark: #b8861a;
    --star-edge: #8e6a1e;
    --rule-gold: #f3c21c;
  }
  * { margin: 0; padding: 0; box-sizing: border-box; }
  html, body { width: 1200px; height: 1000px; overflow: hidden; background: var(--paper); }
  body { position: relative; font-family: "Sansita", Georgia, serif; }

  .spread { position: absolute; left: 28px; top: 0; width: 960px; height: 752px; }

  .panel {
    position: absolute; top: 0; height: 752px;
    background: linear-gradient(to bottom,
      var(--paper) 0%, var(--paper) 42%,
      var(--gold-pale) 55%, var(--gold) 72%,
      var(--gold-deep) 86%, var(--gold-amber) 100%);
  }
  .back-cover { left: 0; width: 454px; }
  .spine { left: 456px; width: 48px; }
  .front-cover { left: 508px; width: 452px; }

  .rule { position: absolute; height: 4px; background: var(--rule-gold); }
  .rule.thin { height: 2px; }
  .base-band { position: absolute; left: 0; right: 0; top: 718px; height: 34px; background: var(--gold-amber); }

  .stars { position: absolute; }
  .laurel {
    position: absolute; border-radius: 50%;
    background: linear-gradient(to right, rgba(214,159,46,0), var(--star-dark) 30%, var(--star-light) 50%, var(--star-dark) 70%, rgba(214,159,46,0));
    opacity: .85;
  }

  /* back cover header */
  .back-series {
    position: absolute; left: 0; width: 454px; top: 80px; text-align: center;
    font-weight: 800; font-size: 14px; color: var(--gold-deep); letter-spacing: .3px;
  }
  .back-subtitle {
    position: absolute; left: 0; width: 454px; top: 98px; text-align: center;
    font-weight: 800; font-size: 13px; line-height: 14px; color: var(--bronze);
  }

  /* spine */
  .spine-title {
    position: absolute; top: 62px; left: 6px; height: 300px;
    writing-mode: vertical-rl; font-weight: 800; font-size: 11px; line-height: 12px;
    color: var(--bronze);
  }
  .spine-author {
    position: absolute; top: 568px; left: 14px; height: 172px;
    writing-mode: vertical-rl; transform: rotate(180deg);
    font-weight: 800; font-size: 15px; color: var(--paper); letter-spacing: .5px;
  }

  /* front cover */
  .front-series {
    position: absolute; left: 0; width: 452px; top: 124px; text-align: center;
    font-weight: 800; font-size: 21px; color: var(--gold-deep); letter-spacing: .5px;
  }
  .numeral-five {
    position: absolute; left: 138px; top: 212px; width: 200px;
    font-weight: 900; font-size: 330px; line-height: 1; text-align: center;
    color: rgba(240, 197, 55, .12);
  }
  .front-title {
    position: absolute; left: 0; width: 452px; top: 278px; text-align: center;
    font-weight: 800; font-size: 29px; line-height: 30px; color: var(--title-gold);
  }
  .front-title .accent { color: var(--bronze-dark); }
  .author-label {
    position: absolute; left: 0; width: 452px; top: 674px; text-align: center;
    font-weight: 800; font-size: 18px; color: var(--bronze);
  }
  .author-name {
    position: absolute; left: 0; width: 452px; top: 697px; text-align: center;
    font-weight: 800; font-size: 19px; color: var(--bronze-dark);
  }
</style>
</head>
<body>
<svg width="0" height="0" style="position:absolute">
  <defs>
    <linearGradient id="starFill" x1="0" y1="0" x2="1" y2="1">
      <stop offset="0" stop-color="#f9dc78"/>
      <stop offset=".55" stop-color="#e2b23a"/>
      <stop offset="1" stop-color="#b8861a"/>
    </linearGradient>
    <symbol id="star" viewBox="0 0 100 100">
      <polygon points="50,4 61,37 96,37 68,58 79,93 50,72 21,93 32,58 4,37 39,37"
        fill="url(#starFill)" stroke="#8e6a1e" stroke-width="4" stroke-linejoin="round"/>
    </symbol>
  </defs>
</svg>

<div class="spread">
  <section class="panel back-cover">
    <svg class="stars" style="left:165px;top:44px" width="126" height="34" viewBox="0 0 126 34">
      <use href="#star" x="2" y="6" width="16" height="16"/>
      <use href="#star" x="22" y="3" width="22" height="22"/>
      <use href="#star" x="48" y="0" width="28" height="28"/>
      <use href="#star" x="82" y="3" width="22" height="22"/>
      <use href="#star" x="108" y="6" width="16" height="16"/>
    </svg>
    <div class="laurel" role="img" aria-label="Gold laurel branches beneath the stars" style="left:150px;top:66px;width:154px;height:10px"></div>
    <div class="back-series">STANDING GROWTH</div>
    <div class="back-subtitle">Keys to Glowing Customer Ratings<br>That Fill The Calendar and Draw Fresh Clients Through Every Entrance!</div>
    <div class="rule" style="left:0;width:454px;top:138px"></div>
    <div class="rule thin" style="left:0;width:454px;top:146px"></div>
    <div class="rule" style="left:0;width:454px;top:708px"></div>
    <div class="base-band"></div>
  </section>

  <section class="panel spine">
    <div class="spine-title">Keys to Glowing Customer Ratings<br>That Fill The Calendar and Draw Fresh Clients</div>
    <div class="spine-author">Fireman Dale Orsworth</div>
  </section>

  <section class="panel front-cover">
    <svg class="stars" style="left:104px;top:46px" width="244" height="58" viewBox="0 0 244 58">
      <use href="#star" x="0" y="14" width="30" height="30"/>
      <use href="#star" x="40" y="6" width="42" height="42"/>
      <use href="#star" x="92" y="0" width="56" height="56"/>
      <use href="#star" x="158" y="6" width="42" height="42"/>
      <use href="#star" x="212" y="14" width="30" height="30"/>
    </svg>
    <div class="laurel" role="img" aria-label="Gold laurel branches curving beneath the five stars" style="left:66px;top:86px;width:320px;height:20px"></div>
    <div class="rule" style="left:0;width:86px;top:130px"></div>
    <div class="rule thin" style="left:0;width:86px;top:138px"></div>
    <div class="rule" style="left:364px;width:88px;top:130px"></div>
    <div class="rule thin" style="left:364px;width:88px;top:138px"></div>
    <div class="front-series">STANDING GROWTH</div>

    <div class="numeral-five" aria-hidden="true">5</div>
    <h1 class="front-title">
      <span class="accent">Keys to</span> Glowing Customer<br>
      Ratings <span class="accent">That</span><br>
      <span class="accent">Fill The Calendar</span><br>
      <span class="accent">and</span><br>
      <span class="accent">Draw Fresh Clients</span><br>
      <span class="accent">Through Every Entrance!</span>
    </h1>

    <div class="author-label">Author</div>
    <div class="author-name">Fireman Dale Orsworth</div>
    <div class="rule" style="left:0;width:84px;top:708px"></div>
    <div class="rule" style="left:362px;width:90px;top:708px"></div>
    <div class="base-band"></div>
  </section>
</div>
</body>
</html>
```